Classy, Elegant, Simple Business Card Design

Looking to have a classy, simple, and elegant design. Want a top notch designed business card. I really like the look of the new brivo credit card. I also like the design I attached. I am trying to reach 21-29 year old females for booking us for there wedding or event. We offer Disc Jockey Service, Photo Booth Rentals, and Uplighting .

Target Market(s)

21-28 year old females

Contact Information for Business Card

Has to have logo, website, email, and phone number

Font styles to use
Other font styles liked:
• open to font choice, modern, clean
Designer to choose
33a6d7
0791cd
0555a3
ffffff

Requirements
Must have
• Has to have logo, website, email, and phone number
Nice to have
• I really like the design of the new brivo credit card. I also included my logo and some designs I like
Should not have
• clutter or too much info

```html
<!DOCTYPE html>
<html lang="en">
<head>
<meta charset="utf-8">
<title>Tidewell Event Group – Business Card</title>
<link rel="stylesheet" href="https://fonts.googleapis.com/css2?family=Montserrat:wght@400;600;700&family=Roboto:wght@400;500&display=swap">
<style>
  :root {
    --navy: #15305a;
    --navy-deep: #0e2447;
    --blue: #0791cd;
    --blue-mid: #0555a3;
    --sky: #33a6d7;
    --white: #ffffff;
    --ink: #3c4048;
    --grey: #6b7078;
    --stage: #e9ebee;
  }
  * { box-sizing: border-box; margin: 0; padding: 0; }
  html, body { width: 1200px; height: 912px; overflow: hidden; }
  body { background: var(--stage); position: relative; font-family: "Roboto", sans-serif; }

  .card {
    position: absolute;
    width: 540px;
    height: 310px;
    border-radius: 18px;
    overflow: hidden;
    box-shadow: 0 6px 18px rgba(0,0,0,0.12);
  }

  /* Back side */
  .card--back { left: 90px; top: 100px; background: var(--navy); color: var(--white); }
  .card--back .brand {
    position: absolute; left: 0; right: 0; top: 112px;
    display: flex; align-items: center; justify-content: center; gap: 14px;
  }
  .brand-dot { width: 18px; height: 18px; border-radius: 50%; background: var(--sky); }
  .brand-name {
    font-family: "Montserrat", sans-serif; font-weight: 600;
    font-size: 34px; letter-spacing: 3px; line-height: 1.15; text-align: left;
  }
  .card--back .brand-name { color: var(--white); }
  .card--back .brand-name small { display: block; font-size: 14px; letter-spacing: 6px; }
  .card--back .site {
    position: absolute; left: 0; right: 0; bottom: 34px; text-align: center;
    font-size: 16px; letter-spacing: 2px; color: var(--white);
  }

  /* Front side */
  .card--front { left: 570px; top: 500px; background: var(--white); }
  .card--front .brand {
    position: absolute; left: 30px; top: 118px; width: 230px;
    display: flex; align-items: center; gap: 12px;
  }
  .card--front .brand-name { color: var(--blue-mid); font-size: 26px; letter-spacing: 2px; }
  .card--front .brand-name small { display: block; font-size: 11px; letter-spacing: 5px; }
  .divider { position: absolute; left: 285px; top: 50px; width: 1px; height: 170px; background: var(--blue); }

  .details { position: absolute; left: 306px; top: 46px; color: var(--ink); font-size: 13px; line-height: 1.45; }
  .person-name { font-family: "Montserrat", sans-serif; font-weight: 700; font-size: 20px; color: var(--blue); letter-spacing: 0.5px; }
  .person-role { color: var(--grey); font-size: 13px; margin-bottom: 10px; }
  .address { margin-bottom: 10px; }
  .contact-list { list-style: none; }
  .contact-list li { display: flex; align-items: center; gap: 8px; }
  .contact-list svg { width: 11px; height: 11px; flex: none; }
  .contact-list .hl { color: var(--blue-mid); font-weight: 500; }

  .swoosh { position: absolute; left: 0; bottom: 0; width: 540px; height: 310px; }
</style>
</head>
<body>

  <section class="card card--back" aria-label="Business card back">
    <div class="brand">
      <span class="brand-dot"></span>
      <div class="brand-name">TIDEWELL<small>EVENT GROUP</small></div>
    </div>
    <p class="site">www.tidewell.com</p>
  </section>

  <section class="card card--front" aria-label="Business card front">
    <svg class="swoosh" viewBox="0 0 540 310" aria-hidden="true">
      <path d="M300 310 C380 270 470 230 540 170 L540 310 Z" fill="var(--navy-deep)"/>
      <path d="M285 310 C370 265 460 215 520 165 C470 220 390 270 305 310 Z" fill="var(--blue)"/>
    </svg>

    <div class="brand">
      <span class="brand-dot"></span>
      <div class="brand-name">TIDEWELL<small>EVENT GROUP</small></div>
    </div>

    <div class="divider"></div>

    <div class="details">
      <p class="person-name">DANIEL HART</p>
      <p class="person-role">Managing Partner</p>
      <p class="address">418 W Harbor Ave.,<br>Pasadena, CA 91105</p>
      <ul class="contact-list">
        <li>
          <svg viewBox="0 0 12 12"><path d="M3 1 L5 3.5 L4 5 C5 7 6 8 7 8.5 L8.5 7.5 L11 9.5 L10 11 C5 11 1 7 1 2 Z" fill="var(--blue)"/></svg>
          555-204-7190
        </li>
        <li>
          <svg viewBox="0 0 12 12"><rect x="1" y="2.5" width="10" height="7" fill="none" stroke="var(--blue)" stroke-width="1.2"/><path d="M1 2.5 L6 6.5 L11 2.5" fill="none" stroke="var(--blue)" stroke-width="1.2"/></svg>
          info@tidewell.com
        </li>
        <li>
          <svg viewBox="0 0 12 12"><circle cx="6" cy="6" r="5" fill="none" stroke="var(--blue)" stroke-width="1.1"/><path d="M1 6 H11 M6 1 C3.5 3.5 3.5 8.5 6 11 M6 1 C8.5 3.5 8.5 8.5 6 11" fill="none" stroke="var(--blue)" stroke-width="0.9"/></svg>
          <span>www.<span class="hl">tidewell</span>.com</span>
        </li>
      </ul>
    </div>
  </section>

</body>
</html>
```